Wedding Startup Full Website Design

We've just completed our online platform and need to create a website that represents our brand and vision, and clearly communicates our features and value proposition to potential users. There are a minimum of 4 pages that need to be designed. One geared toward wedding professionals (venues/vendors/coordinators), another toward engaged couples, one showcasing features, and an 'About Us' page.

The designer will creative freedom to create a unique UI/UX as long as it represents our brand and is relevant to our target audience/market. The ideal candidate will be able to assume the mindset of someone working in the wedding industry and/or an engaged couple. Ability to create illustrations is a plus.

Copy will be provided as needed. We will reimburse for stock images (pending approval before purchasing), but sourcing the stock images will be the responsibility of the designer.

Our current website: https://www.marquiso.com
Updates

Still waiting for a design that stands out from the rest and aligns with the creative brief.

Target Market(s)

Wedding Professionals and Engaged Couples

Industry/Entity Type

Wedding

Number of Pages Required

4 page

Font styles to use
Sans Serif

Colors
ffffff
fbd4d5
f59195
33a6d7
cadf82
86cfc6

Requirements
Must have
• Common sense stuff like having a unified brand that accurately represents our platform, speaks to our target market, and clearly articulates our vision
Nice to have
• Illustrations
Should not have
• Overly cheesy or childish. We want to be professional but still embrace the wedding culture.

```html
<!DOCTYPE html>
<html lang="en">
<head>
<meta charset="utf-8">
<title>Marquiso — Wedding Plans, Simplified</title>
<link href="https://fonts.googleapis.com/css2?family=Montserrat:wght@400;600;700&family=Open+Sans:wght@400;600;700&family=Great+Vibes&display=swap" rel="stylesheet">
<style>
:root{
  --blue:#33a6d7;
  --blue-light:#4fbbe6;
  --blue-deep:#1f8fc4;
  --ink:#2d3a45;
  --text:#6f7780;
  --muted:#a3a9ae;
  --line:#e3e6e9;
  --panel:#f3f5f7;
  --white:#ffffff;
  --blush:#fbd4d5;
  --rose:#f59195;
  --footer:#2b3540;
  --tick:#8bc34a;
}
*{box-sizing:border-box;margin:0;padding:0}
html,body{width:1200px;height:5114px;overflow:hidden;background:var(--white)}
body{position:relative;font-family:"Open Sans",Arial,sans-serif;color:var(--text)}
.abs{position:absolute}
.photo{position:absolute}
h2,.title{font-family:"Montserrat",Arial,sans-serif;color:var(--ink);font-weight:600}
.btn{position:absolute;display:flex;align-items:center;justify-content:center;background:var(--blue-light);color:var(--white);font-family:"Montserrat",Arial,sans-serif;font-weight:700;font-size:12px;letter-spacing:1px;border-radius:22px;text-transform:uppercase;white-space:nowrap}

/* hero */
.hero{position:absolute;left:0;top:0;width:1200px;height:560px;
  background:linear-gradient(100deg,#3e4a36 0%,#6b7550 30%,#c9c2b0 55%,#7f6a58 72%,#3d3a33 100%)}
.hero-shade{position:absolute;inset:0;background:linear-gradient(180deg,rgba(0,0,0,.25),rgba(0,0,0,0) 30%,rgba(0,0,0,.35))}
.nav{position:absolute;top:26px;left:0;width:1200px;height:40px}
.brand{position:absolute;font-family:"Montserrat",Arial,sans-serif;font-weight:600;color:var(--white);font-size:26px;display:flex;align-items:center;gap:8px}
.brand .dot{width:10px;height:10px;border-radius:50%;background:var(--white)}
.nav-links{position:absolute;right:230px;top:10px;display:flex;gap:34px;font-family:"Montserrat",Arial,sans-serif;font-size:11px;font-weight:600;color:var(--white);letter-spacing:1px}
.hero-welcome{position:absolute;left:102px;top:348px;color:var(--white);font-family:"Montserrat",Arial,sans-serif;font-size:19px;font-weight:600}
.hero-script{position:absolute;left:100px;top:378px;color:var(--white);font-family:"Great Vibes",cursive;font-size:56px;line-height:1;white-space:nowrap}
.slider-dots{position:absolute;right:88px;top:250px;display:flex;flex-direction:column;gap:8px}
.slider-dots i{width:8px;height:8px;border-radius:50%;border:1px solid var(--white)}
.slider-dots i.on{background:var(--white)}
.scallop{position:absolute;left:0;width:1200px;height:14px;
  background:radial-gradient(circle at 8px 14px,var(--white) 8px,transparent 8.5px) 0 0/16px 14px repeat-x}

/* steps */
.section-title{position:absolute;left:0;width:1200px;text-align:center;font-size:32px}
.step-icon{position:absolute;width:180px;text-align:center}
.step-num{width:36px;height:36px;margin:0 auto 18px;border-radius:50%;border:1px solid var(--line);font-size:11px;color:var(--muted);display:flex;align-items:center;justify-content:center;font-family:"Montserrat",Arial,sans-serif}
.step-glyph{display:block;margin:0 auto 14px}
.step-name{font-family:"Montserrat",Arial,sans-serif;font-size:20px;font-weight:600;color:var(--ink);margin-bottom:8px}
.step-desc{font-size:13px;line-height:1.55;color:var(--text)}
.step-link{font-size:13px;color:var(--blue);margin-top:16px}
.screen{position:absolute;background:var(--white);border:1px solid var(--line);box-shadow:0 8px 30px rgba(40,60,80,.12);overflow:hidden}
.screen .bar{position:absolute;height:9px;border-radius:2px;background:#d5dade}
.screen .bar.lt{background:#e8ebee}
.screen .side{position:absolute;left:0;top:0;bottom:0;background:var(--panel);border-right:1px solid var(--line)}
.screen .top{position:absolute;left:0;right:0;top:0;height:40px;background:#e9f4fa;border-bottom:1px solid var(--line)}
.pay-name{font-family:"Montserrat",Arial,sans-serif;font-weight:600;font-size:20px;color:var(--ink);margin-bottom:8px}

/* why */
.why-rule{position:absolute;left:0;top:2236px;width:200px;height:2px;background:var(--blue)}
.why-intro{position:absolute;left:232px;top:2278px;width:420px;font-size:13px;line-height:1.6}
.diamond{position:absolute;width:250px;height:250px}
.diamond .shape{position:absolute;left:38px;top:38px;width:174px;height:174px;transform:rotate(45deg);background:var(--white);box-shadow:0 6px 26px rgba(40,60,80,.14)}
.diamond .badge{position:absolute;left:100px;top:12px;width:50px;height:50px;transform:rotate(45deg);background:var(--blue-light);box-shadow:0 4px 12px rgba(51,166,215,.4)}
.diamond .ico{position:absolute;left:112px;top:24px}
.diamond .txt{position:absolute;left:55px;top:82px;width:140px;text-align:center}
.diamond h3{font-family:"Montserrat",Arial,sans-serif;font-size:12px;font-weight:600;color:var(--ink);margin-bottom:6px;white-space:nowrap}
.diamond p{font-size:9.5px;line-height:1.5;color:var(--text)}
.diamond.gray .shape{background:#f5f6f7}

/* mission */
.mission-box{position:absolute;left:275px;top:3098px;width:650px;height:228px;background:rgba(51,166,215,.88);color:var(--white);text-align:center;padding:30px 48px}
.mission-box::before{content:"";position:absolute;inset:8px;border:1px solid rgba(255,255,255,.7)}
.mission-box h2{color:var(--white);font-size:28px;margin-bottom:16px}
.mission-box p{font-size:12.5px;line-height:1.6;margin-bottom:10px}

/* reviews */
.review-text{position:absolute;left:250px;top:3700px;width:700px;text-align:center;font-size:13px;line-height:1.65}
.review-name{position:absolute;left:0;width:1200px;top:3808px;text-align:center;color:var(--blue);font-size:13px}
.arrow{position:absolute;top:3720px}

/* video */
.video-word{position:absolute;left:0;width:1200px;top:3850px;text-align:center;font-family:"Montserrat",Arial,sans-serif;font-size:96px;font-weight:700;color:#f1f3f5;letter-spacing:4px}
.feature{position:absolute;width:250px;text-align:center;color:var(--white)}
.feature h3{font-family:"Montserrat",Arial,sans-serif;font-size:14px;font-weight:600;margin:12px 0 8px}
.feature p{font-size:11px;line-height:1.55;color:rgba(255,255,255,.85)}

/* cta */
.cta-text{position:absolute;left:250px;top:4770px;width:700px;text-align:center;font-size:13px;line-height:1.6}

/* footer */
.footer{position:absolute;left:0;top:4944px;width:1200px;height:170px;background:var(--footer)}
.footer .nav-links{right:230px;top:40px;color:#c9d0d6;font-weight:400}
.footer-rule{position:absolute;left:100px;right:100px;top:100px;height:1px;background:#44505b}
.footer-copy{position:absolute;top:126px;font-size:10px;color:#8b959e}
.socials{position:absolute;left:0;width:1200px;top:120px;display:flex;justify-content:center;gap:10px}
.socials i{width:24px;height:24px;border-radius:50%;border:1px solid #8b959e}
</style>
</head>
<body>

<!-- Hero -->
<section class="hero" role="img" aria-label="Photo of a bride and groom kissing outdoors by a stone wall, bride holding an orange bouquet">
  <div class="hero-shade"></div>
</section>
<header class="nav">
  <div class="brand" style="left:100px;top:0"><span class="dot"></span>Marquiso</div>
  <nav class="nav-links"><span>ABOUT</span><span>OUR FEATURES</span><span>THE COURSES</span></nav>
  <div class="btn" style="right:100px;top:0;width:110px;height:34px;font-size:10px">Sign Up Free</div>
</header>
<div class="hero-welcome">Welcome to Marquiso</div>
<div class="hero-script">Wedding Plans, Simplified</div>
<div class="btn" style="left:395px;top:458px;width:80px;height:26px;font-size:8px">Get Started</div>
<div class="slider-dots"><i class="on"></i><i></i><i></i></div>
<div class="scallop" style="top:546px"></div>

<!-- How to get started -->
<h2 class="section-title title" style="top:610px">How To Get Started</h2>

<div class="photo" style="left:0;top:720px;width:320px;height:410px;background:linear-gradient(135deg,#e9e3da,#b88e74 45%,#5b4a44 80%,#8a8f9a)" role="img" aria-label="Photo of a smiling couple looking at a tablet together on a sofa"></div>
<div class="step-icon" style="left:353px;top:708px">
  <div class="step-num">01</div>
  <svg class="step-glyph" width="64" height="66" viewBox="0 0 64 66"><circle cx="32" cy="18" r="16" fill="#33a6d7"/><path d="M2 66c0-20 13-30 30-30s30 10 30 30z" fill="#33a6d7"/></svg>
  <div class="step-name">Sign Up</div>
  <div class="step-desc">Create a free account on Marquiso to access popular collaboration tools.</div>
  <div class="step-link">Get Started</div>
</div>
<div class="screen" style="left:672px;top:710px;width:528px;height:420px">
  <div class="side" style="width:70px"></div>
  <div class="abs" style="left:100px;top:22px;font-size:13px;color:var(--ink)">Jordan Ellis</div>
  <div class="bar lt" style="left:100px;top:52px;width:400px"></div>
  <div class="abs" style="left:100px;top:85px;font-size:12px;color:var(--ink)">Ceremony Guidelines</div>
  <div class="bar" style="left:100px;top:112px;width:400px"></div>
  <div class="bar lt" style="left:100px;top:132px;width:360px"></div>
  <div class="bar lt" style="left:100px;top:180px;width:400px"></div>
  <div class="bar lt" style="left:100px;top:200px;width:380px"></div>
  <div class="bar lt" style="left:100px;top:220px;width:250px"></div>
  <div class="bar" style="left:100px;top:280px;width:300px"></div>
  <div class="bar lt" style="left:100px;top:302px;width:400px"></div>
  <div class="bar" style="left:100px;top:350px;width:400px"></div>
  <div class="bar lt" style="left:100px;top:372px;width:340px"></div>
  <div class="bar lt" style="left:14px;top:60px;width:42px"></div>
  <div class="bar lt" style="left:14px;top:90px;width:42px"></div>
  <div class="bar lt" style="left:14px;top:120px;width:42px"></div>
  <div class="bar lt" style="left:14px;top:150px;width:42px"></div>
</div>

<div class="screen" style="left:0;top:1196px;width:528px;height:400px">
  <div class="top"></div>
  <div class="abs" style="left:14px;top:12px;font-size:13px;color:var(--ink)">Inbox&nbsp;&nbsp;&nbsp;&nbsp;Groups</div>
  <div class="side" style="top:40px;width:120px"></div>
  <div class="bar lt" style="left:12px;top:70px;width:90px"></div>
  <div class="bar lt" style="left:12px;top:100px;width:90px"></div>
  <div class="bar lt" style="left:12px;top:130px;width:90px"></div>
  <div class="bar lt" style="left:12px;top:160px;width:90px"></div>
  <div class="bar lt" style="left:12px;top:190px;width:90px"></div>
  <div class="abs" style="left:140px;top:80px;width:360px;height:110px;background:var(--panel)"></div>
  <div class="abs" style="left:140px;top:210px;width:210px;height:160px;background:#e6e9ec"></div>
  <div class="bar lt" style="left:370px;top:220px;width:130px"></div>
  <div class="bar lt" style="left:370px;top:240px;width:110px"></div>
  <div class="abs" style="left:465px;top:350px;width:26px;height:26px;border-radius:50%;background:var(--blue-light)"></div>
</div>
<div class="step-icon" style="left:667px;top:1196px">
  <div class="step-num">02</div>
  <svg class="step-glyph" width="76" height="66" viewBox="0 0 76 66"><circle cx="38" cy="10" r="9" fill="#33a6d7"/><path d="M24 36c0-10 6-15 14-15s14 5 14 15z" fill="#33a6d7"/><circle cx="16" cy="44" r="9" fill="#33a6d7"/><path d="M2 66c0-10 6-14 14-14s14 4 14 14z" fill="#33a6d7"/><circle cx="60" cy="44" r="9" fill="#33a6d7"/><path d="M46 66c0-10 6-14 14-14s14 4 14 14z" fill="#33a6d7"/><circle cx="38" cy="44" r="9" fill="#33a6d7"/><path d="M24 66c0-10 6-14 14-14s14 4 14 14z" fill="#33a6d7"/></svg>
  <div class="step-name">Collaborate</div>
  <div class="step-desc">Add clients within the application to better organize and manage event details.</div>
</div>
<div class="photo" style="left:890px;top:1210px;width:310px;height:400px;background:linear-gradient(135deg,#f2f2f2,#b7a698 40%,#3b3a44 75%,#d8d2cc)" role="img" aria-label="Photo of three smiling business people, wedding professionals, standing together"></div>

<div class="photo" style="left:0;top:1655px;width:320px;height:440px;background:linear-gradient(135deg,#f0f0f0,#c7967e 40%,#6a4a3c 70%,#9aa0a6)" role="img" aria-label="Photo of a smiling woman pointing to the side"></div>
<div class="step-icon" style="left:353px;top:1672px">
  <div class="step-num">03</div>
  <svg class="step-glyph" width="64" height="66" viewBox="0 0 64 66"><circle cx="32" cy="18" r="16" fill="#33a6d7"/><path d="M2 66c0-20 13-30 30-30s30 10 30 30z" fill="#33a6d7"/></svg>
  <div class="step-name">Connect</div>
  <div class="step-desc">Linking your bank account within Marquiso to allow for seamless payments and reconciling.</div>
</div>
<div class="screen" style="left:672px;top:1690px;width:528px;height:405px;background:var(--panel)">
  <div class="abs" style="left:20px;top:20px;font-size:14px;color:var(--muted)">Finance</div>
  <div class="abs" style="left:20px;top:60px;width:80px;height:300px;background:#e9ecef"></div>
  <div class="abs" style="left:20px;top:300px;font-size:20px;color:#9aa3ab">$13,03.54</div>
  <div class="abs" style="left:175px;top:40px;width:340px;height:320px;background:var(--white);box-shadow:0 8px 26px rgba(0,0,0,.15);padding:26px 24px">
    <svg width="34" height="26" viewBox="0 0 34 26" style="display:block;margin:0 auto 12px"><path d="M3 13l10 10L31 3" fill="none" stroke="#8bc34a" stroke-width="4"/></svg>
    <div style="text-align:center;font-family:Montserrat,Arial,sans-serif;font-weight:700;font-size:17px;color:var(--ink);margin-bottom:8px">All Done!</div>
    <div style="text-align:center;font-size:12px;line-height:1.5;color:var(--text);margin-bottom:18px">Your account has been successfully setup and is now able to receive payments.</div>
    <div class="pay-name">Fundrail</div>
    <div style="font-size:10px;line-height:1.5;color:var(--text)">Through our integration with Fundrail, your information is protected by industry leading cyber security. All of your deposits go straight into your linked bank account.</div>
    <div style="text-align:right;font-size:10px;color:var(--blue);margin-top:10px">Continue</div>
  </div>
</div>

<!-- Why choose -->
<div class="why-rule"></div>
<h2 class="title abs" style="left:232px;top:2200px;font-size:32px">Why Choose Marquiso</h2>
<p class="why-intro">Class aptent taciti sociosqu ad litora torquent per conubia nostra, per inceptos himenaeos. Mauris in erat justo. Nullam ac urna eu felis dapibus condimentum sit.</p>
<div class="photo" style="left:680px;top:2114px;width:520px;height:400px;background:radial-gradient(ellipse at 60% 40%,#eae6e0 0%,#c9b8a6 40%,rgba(255,255,255,0) 72%)" role="img" aria-label="Photo of a bride hugging a bridesmaid, fading into white"></div>

<div class="diamond" style="left:82px;top:2398px"><div class="shape"></div><div class="badge"></div>
  <svg class="ico" width="26" height="26" viewBox="0 0 26 26"><circle cx="13" cy="13" r="10" fill="none" stroke="#fff" stroke-width="2"/><path d="M13 7v6l4 3" fill="none" stroke="#fff" stroke-width="2"/></svg>
  <div class="txt"><h3>Saves Everyone Time</h3><p>Marquiso streamlines event planning by giving every person one shared hub, so less time goes to back and forth.</p></div></div>
<div class="diamond" style="left:433px;top:2398px"><div class="shape"></div><div class="badge"></div>
  <svg class="ico" width="26" height="26" viewBox="0 0 26 26"><rect x="3" y="5" width="20" height="13" rx="2" fill="none" stroke="#fff" stroke-width="2"/><path d="M8 18l-2 5 6-5" fill="#fff"/></svg>
  <div class="txt"><h3>Better Client Reviews</h3><p>With Marquiso you can offer your clients an experience they will rave about, leading to better reviews and more sales.</p></div></div>
<div class="diamond" style="left:727px;top:2398px"><div class="shape"></div><div class="badge"></div>
  <svg class="ico" width="26" height="26" viewBox="0 0 26 26"><rect x="3" y="4" width="20" height="14" rx="1" fill="none" stroke="#fff" stroke-width="2"/><path d="M9 22h8M13 18v4" stroke="#fff" stroke-width="2"/></svg>
  <div class="txt"><h3>Accessible on Any Device</h3><p>Flexibility is key, which is why the platform looks great on a computer, phone, tablet or desktop.</p></div></div>
<div class="diamond gray" style="left:284px;top:2568px"><div class="shape"></div><div class="badge"></div>
  <svg class="ico" width="26" height="26" viewBox="0 0 26 26"><path d="M4 6h18M4 13h18M4 20h18" stroke="#fff" stroke-width="2"/></svg>
  <div class="txt"><h3>Simplified Organization</h3><p>Marquiso was built with organization in mind. All event details are in one place, making planning easier.</p></div></div>
<div class="diamond" style="left:574px;top:2568px"><div class="shape photo" role="img" aria-label="Photo of a decorated wedding reception table with candles and flowers" style="background:radial-gradient(circle at 50% 50%,#d9b98a,#6e5a48 60%,#3c3530);box-shadow:0 6px 26px rgba(40,60,80,.2)"></div></div>
<div class="diamond gray" style="left:881px;top:2568px"><div class="shape"></div><div class="badge"></div>
  <svg class="ico" width="26" height="26" viewBox="0 0 26 26"><text x="13" y="19" text-anchor="middle" font-family="Montserrat,Arial,sans-serif" font-size="17" font-weight="700" fill="#fff">$</text></svg>
  <div class="txt"><h3>Lower Transaction Fees</h3><p>We offer the lowest online processing fees, so more of the wedding proceeds stay in your pocket.</p></div></div>

<!-- Mission -->
<div class="photo" style="left:0;top:2918px;width:1200px;height:460px;background:linear-gradient(100deg,#6d7a52,#c9b59c 30%,#e8ddd0 50%,#a99078 70%,#56623f)" role="img" aria-label="Photo of joyful wedding guests cheering and throwing petals at a newly married couple"></div>
<div class="mission-box">
  <h2>Mission Statement</h2>
  <p>Weddings are the most memorable events in people's life. Unfortunately planning a wedding is filled with stress, often leaving wedding professionals and their clients with soured memories.</p>
  <p>Our vision at Marquiso is to revolutionize the way weddings are planned on both sides of the process (wedding professionals and their clients). We aim to reduce the stress of everyone involved and make the engagement season &amp; wedding day memorable for the right reasons.</p>
</div>

<!-- Reviews -->
<div class="photo" style="left:450px;top:3470px;width:300px;height:150px;background:radial-gradient(ellipse at center,#e6e6e6,rgba(255,255,255,0) 70%)" role="img" aria-label="Faded photo of a wedding couple"></div>
<svg class="abs" style="left:578px;top:3580px" width="44" height="34" viewBox="0 0 44 34"><path d="M2 34V18C2 8 8 2 18 0v6c-5 2-8 6-8 12h8v16zM26 34V18c0-10 6-16 16-18v6c-5 2-8 6-8 12h8v16z" fill="#33a6d7"/></svg>
<h2 class="section-title title" style="top:3630px">Happy Customer Reviews</h2>
<p class="review-text">"Class aptent taciti sociosqu ad litora torquent per conubia nostra, per inceptos himenaeos. Mauris in erat justo. Nullam ac urna eu felis dapibus condimentum sit amet a augue. Sed non neque elit. Sed ut imperdiet nisi. Proin condimentum fermentum nunc. Etiam pharetra, erat sed fermentum feugiat, velit mauris egestas quam, ut aliquam massa nisl quis neque. Suspendisse in orci enim."</p>
<div class="review-name">— Mara Quinn</div>
<svg class="arrow" style="left:82px" width="16" height="28" viewBox="0 0 16 28"><path d="M14 2L2 14l12 12" fill="none" stroke="#b9bfc4" stroke-width="2"/></svg>
<svg class="arrow" style="left:1102px" width="16" height="28" viewBox="0 0 16 28"><path d="M2 2l12 12L2 26" fill="none" stroke="#b9bfc4" stroke-width="2"/></svg>

<!-- Video + features -->
<div class="video-word">WATCH VIDEO</div>
<svg class="abs" style="left:0;top:4040px" width="1200" height="610" viewBox="0 0 1200 610"><defs><linearGradient id="blueband" x1="0" y1="0" x2="0" y2="1"><stop offset="0" stop-color="#4fbbe6"/><stop offset="1" stop-color="#2f9fd2"/></linearGradient></defs><path d="M0 60 Q600 -40 1200 60 V610 H0z" fill="url(#blueband)"/></svg>
<div class="photo" style="left:239px;top:3955px;width:722px;height:392px;background:linear-gradient(120deg,#7a8a8e,#d2cbc4 40%,#4a4540 70%,#8f9a8a)" role="img" aria-label="Video still of a bride and groom embracing outdoors"></div>
<svg class="abs" style="left:570px;top:4121px" width="60" height="60" viewBox="0 0 60 60"><circle cx="30" cy="30" r="28" fill="rgba(0,0,0,.25)" stroke="#fff" stroke-width="3"/><path d="M24 18l18 12-18 12z" fill="#fff"/></svg>

<div class="feature" style="left:176px;top:4408px">
  <svg width="34" height="30" viewBox="0 0 34 30"><circle cx="12" cy="9" r="6" fill="none" stroke="#fff" stroke-width="2"/><circle cx="24" cy="9" r="6" fill="none" stroke="#fff" stroke-width="2"/><path d="M2 28c0-7 5-11 10-11s10 4 10 11M14 28c0-7 5-11 10-11s8 4 8 11" fill="none" stroke="#fff" stroke-width="2"/></svg>
  <h3>Realtime Collaboration</h3><p>There are often disconnects in the communication channel. All the users of Marquiso receive updates in realtime to avoid missing information.</p></div>
<div class="feature" style="left:475px;top:4408px">
  <svg width="38" height="30" viewBox="0 0 38 30"><path d="M10 26h20a7 7 0 0 0 0-14 10 10 0 0 0-19-3A8 8 0 0 0 10 26z" fill="none" stroke="#fff" stroke-width="2"/><path d="M19 22V13M15 17l4-4 4 4" fill="none" stroke="#fff" stroke-width="2"/></svg>
  <h3>Cloud Storage</h3><p>No longer do you have to rummage through old documents to find your information. It is stored 100% securely on our servers.</p></div>
<div class="feature" style="left:774px;top:4408px">
  <svg width="30" height="30" viewBox="0 0 30 30"><path d="M6 22V13a9 9 0 0 1 18 0v9l3 3H3z" fill="none" stroke="#fff" stroke-width="2"/><path d="M12 27a3 3 0 0 0 6 0" fill="none" stroke="#fff" stroke-width="2"/></svg>
  <h3>Notifications &amp; Deadlines</h3><p>Every client's dashboard and timeline keeps track of all the information that needs to be completed and updated in a timely manner.</p></div>
<div class="scallop" style="top:4636px"></div>

<!-- CTA -->
<h2 class="section-title title" style="top:4708px;font-size:30px">Get Stated Today!</h2>
<p class="cta-text">We recently launched a demo version of Marquiso to allow users to see and interact with our platform. Create a free account and see how Marquiso is changing the wedding planning process!</p>
<div class="btn" style="left:496px;top:4823px;width:208px;height:40px">Get Started Today!</div>

<!-- Footer -->
<footer class="footer">
  <div class="brand" style="left:100px;top:28px"><span class="dot"></span>Marquiso</div>
  <nav class="nav-links"><span>ABOUT</span><span>OUR FEATURES</span><span>THE COURSES</span></nav>
  <div class="btn" style="right:100px;top:32px;width:110px;height:32px;font-size:10px">Sign Up Free</div>
  <div class="footer-rule"></div>
  <div class="footer-copy" style="left:100px">© 2018 MARQUISO. ALL RIGHTS RESERVED</div>
  <div class="socials"><i></i><i></i><i></i><i></i><i></i><i></i></div>
  <div class="footer-copy" style="right:100px">TERMS OF USE | PRIVACY POLICY | SITEMAP</div>
</footer>

</body>
</html>
```